Fenwick and Ostrander Postcard Design

Greetings!
Lawyers hire me as an expert witness. They take a gamble on hiring me in hopes of winning their case.
This postcard will be printed in jumbo size through Printoria. The design must meet these specifications:

Full Bleed Size (starting document size)
11.12" x 6.12"
282 x 155 mm
3335 x 1835 pixels
* Finished artwork should use the full bleed dimensions for best results.
Document Trim Size (final size after being cut)
11.00" x 6.00"
279 x 152 mm
3300 x 1800 pixels
* Please be sure to keep all text and photos within the safe cutting margin.
Resolution
300 DPI
Visit Printoria for more details or to download a design template:
https://www.printoria-example.com/product-presentation-info.aspx?productPresentationId=2741#
https://www.printoria-example.com/vp/ns/propath/UploadResources.aspx?selectedTab=0?pfid=KRT&pf_id=KRT&xnav=product-page#FileFormats

1. The postcard will have a Blank Backside.
2. I like a black, white and red color theme with a serious legalistic font.
3. In regards to color theme, see https://www.mailerzest-example.com/designs/security-system-postcards/#security-system-postcards-4
4. 8 preferred background images in alphabetical order from favorite to least favorite, but all are great:
a. https://files-example.net/f/s!QwZr83TbLm2uvoxkN7HdY5pW1sgjre
5. Header Text:
a. (line 1) Dr. R.T. Ostrander, Psy.D., ABPP
b. (lines 2 and 3) Psychological Evaluator, Board-Certified Forensic Psychologist and National Expert Witness
c. (Line 4 in bold and more prominent than text in lines 1-3) 4 Signs of a Proficient & Credible Psyc. Expert
6. View this checklist image for inspiration, https://lnkbox-example.net/images/9TqWm3 and use the following text within such a checklist image:
7. Board Certified by the Continental Council of Courtroom Behavioral Science (CCCBS)?
Yes, I'm Board Certified. This mark of proficiency in forensic psychology is recognized by judicial decisions, statutes and regulations.
8. Fellow of the Cont. College of Courtroom Behavioralists?
Yes, I'm a CCCB Fellow, along with some of the field's most prominent leaders comprising the academic arm of the CCCBS.
9. A Recognized Leader Amongst Other Experts?
I’m the 2018 duly elected President of the Empire Region Mental Health Guild Section on Courtroom Behavior, and a Board Member of the National Practitioners Council for Youth Welfare Protection.
10. Positioned in Roles of Trust and Neutrality by Judges?
Yes, I work as an in-house Harbor County Domestic Tribunal mental-health expert in proceedings regarding competency, imminent risk, sentencing, custody, child maltreatment and TPR.
11. The following should be prominent along the bottom:
12. BOOK A LUNCH & LEARN AT YOUR OFFICE
Visit http://offer.benchwise-example.com Call 212-555-0147
Designer: This call to action (CTA) for #12 needs to pop off of the page. It needs to draw the reader's eye. It needs depth, like the way a CTA button looks like on a website. Play around w/ idea to accomplish this (e.g., adding badges, icons, shapes, a picture, an image of someone presenting it, etc).
13. List my areas of specialization somewhere
• CPS & Matrimonial Issues
• Competency
• Juvenile Delinquency
• Criminal Sentencing
• Personal Injury and Civil Rights
• Immigration
• Fitness for Duty, SSD and Workers Comp
• Sex-Offenders
• IME and Neuropsychological Testing
• Behind-The-Scenes Consulting on A Contingency Fee
• Low-Price Initial Screening Evaluations
• Therapy Services & Programs for Litigants
14. Put this test somewhere and keep it subtle: I recognize the importance of your work. You can trust my assistance.
15. Put this in fine print somewhere (can be 2 lines): Fenwick and Ostrander, LLC. 2018 New York Licensed Psychologist Lic. # 047213 - New Jersey Licensed Psychologist Lic. # 72K400915300

Target Market(s)

Lawyers

Industry/Entity Type

Hire

Font styles to use
Serif

Colors
ec1f27
ffffff

Requirements
Must have
• An awesome call to action. If the CTA doesn't catch the eye, then it won't work. The point of this postcard is to get them to that website so I can capture their email address. Anything else is a secondary gain. Consider 3-d design elements to give it pop and depth.
Should not have
• There's a big difference between a red rectangle and a red button on a website that has that 3d quality. This postcard has a lot of words. It can easily become just a bunch of text on a colorful piece of paper w/ a pic. Avoid this by segmenting the space, layering Diff color text on Diff color background and incorporating 3d design elements and shapes.

```html
<!DOCTYPE html>
<html lang="en">
<head>
<meta charset="utf-8">
<title>Fenwick and Ostrander Postcard</title>
<link rel="stylesheet" href="https://fonts.googleapis.com/css2?family=Alegreya:ital,wght@0,400;0,700;0,800;1,400;1,700;1,800&family=Alegreya+SC:wght@700&display=swap">
<style>
  :root {
    --red: #ec1f27;
    --white: #ffffff;
    --black: #0a0a0a;
    --ink: #1e1e1e;
    --canvas: #f3f3f3;
    --row-1: #f4f4f6;
    --row-2: #e9e9eb;
    --row-3: #d7d7d9;
    --row-4: #c4c4c6;
    --wood-light: #a5652e;
    --wood-dark: #3a1c0c;
  }
  * { box-sizing: border-box; margin: 0; padding: 0; }
  html, body { width: 1200px; height: 1000px; overflow: hidden; }
  body { background: var(--canvas); font-family: "Alegreya", Georgia, serif; color: var(--ink); position: relative; }

  .panel { position: absolute; top: 275px; height: 449px; }
  .panel--checklist { left: 192px; width: 393px; background: var(--row-1); }
  .panel--offer { left: 591px; width: 418px; background: var(--black); overflow: hidden; }

  .masthead { height: 105px; background: var(--red); color: var(--white); text-align: center; padding-top: 24px; }
  .masthead__name { font-family: "Alegreya SC", Georgia, serif; font-weight: 700; font-size: 24px; line-height: 1; white-space: nowrap; }
  .masthead__role { font-style: italic; font-weight: 700; font-size: 12.5px; line-height: 15px; margin-top: 11px; white-space: nowrap; }

  .checklist-title { height: 40px; background: var(--white); color: var(--red); font-style: italic; font-weight: 700; font-size: 19.5px; text-align: center; line-height: 40px; white-space: nowrap; }

  .sign { position: relative; padding: 12px 14px 0 62px; }
  .sign:nth-of-type(1) { height: 70px; background: var(--row-1); }
  .sign:nth-of-type(2) { height: 67px; background: var(--row-2); }
  .sign:nth-of-type(3) { height: 80px; background: var(--row-3); }
  .sign:nth-of-type(4) { height: 87px; background: var(--row-4); }
  .sign__tick { position: absolute; left: 18px; top: 50%; width: 28px; height: 28px; margin-top: -16px; }
  .sign__question { font-style: italic; font-weight: 800; font-size: 10.2px; line-height: 13px; color: var(--black); }
  .sign__answer { font-size: 9.6px; line-height: 11.5px; margin-top: 2px; color: #2a2a2a; }

  .hero { position: absolute; left: 0; top: 0; width: 418px; height: 305px; background: linear-gradient(180deg, #5c3a22 0%, #7a4a26 35%, var(--wood-light) 60%, var(--wood-dark) 100%); }
  .hero__tagline { position: absolute; right: 16px; top: 15px; font-style: italic; font-size: 8.5px; color: rgba(255,255,255,0.85); }
  .cta__headline { position: absolute; left: 17px; top: 210px; color: var(--white); font-weight: 800; font-size: 31px; line-height: 36px; text-shadow: 2px 3px 4px rgba(0,0,0,0.85); letter-spacing: -0.3px; white-space: nowrap; }
  .cta__bar { position: absolute; left: 6px; top: 288px; width: 280px; height: 18px; }
  .cta__shape { position: absolute; left: 0; top: 0; }
  .cta__contact { position: absolute; top: 0; height: 18px; font-size: 9px; color: var(--white); display: flex; align-items: center; gap: 6px; white-space: nowrap; }
  .cta__contact svg { flex: none; }
  .cta__contact--web { left: 14px; }
  .cta__contact--phone { left: 196px; }

  .specialties { position: absolute; left: 18px; top: 322px; display: flex; gap: 16px; color: var(--white); font-size: 9.6px; line-height: 11.3px; }
  .specialties ul { list-style: none; }
  .specialties ul:first-child { width: 142px; }
  .fine-print { position: absolute; left: 20px; top: 411px; color: var(--white); font-style: italic; font-size: 10.4px; line-height: 12.5px; white-space: nowrap; }
</style>
</head>
<body>
  <section class="panel panel--checklist">
    <header class="masthead">
      <h1 class="masthead__name">Dr. R.T. Ostrander, Psy.D., ABPP</h1>
      <p class="masthead__role">Psychological Evaluator<br>Board-Certified Forensic Psychologist and National Expert Witness</p>
    </header>
    <h2 class="checklist-title">Signs of a Proficient &amp; Credible Psyc. Expert</h2>
    <div class="signs">
      <article class="sign">
        <svg class="sign__tick" viewBox="0 0 28 28"><circle cx="14" cy="14" r="14" fill="#ec1f27"/><path d="M8 14.5l4 4 8-9" fill="none" stroke="#fff" stroke-width="3" stroke-linecap="round" stroke-linejoin="round"/></svg>
        <p class="sign__question">Board Certified by the Continental Council of Courtroom Behavioral Science (CCCBS)?</p>
        <p class="sign__answer">Yes, I'm Board Certified. This mark of proficiency in forensic psychology is recognized by judicial decisions, statutes and regulations.</p>
      </article>
      <article class="sign">
        <svg class="sign__tick" viewBox="0 0 28 28"><circle cx="14" cy="14" r="14" fill="#ec1f27"/><path d="M8 14.5l4 4 8-9" fill="none" stroke="#fff" stroke-width="3" stroke-linecap="round" stroke-linejoin="round"/></svg>
        <p class="sign__question">Fellow of the Cont. College of Courtroom Behavioralists?</p>
        <p class="sign__answer">Yes, I'm a CCCB Fellow, along with some of the field's most prominent leaders comprising the academic arm of the CCCBS.</p>
      </article>
      <article class="sign">
        <svg class="sign__tick" viewBox="0 0 28 28"><circle cx="14" cy="14" r="14" fill="#ec1f27"/><path d="M8 14.5l4 4 8-9" fill="none" stroke="#fff" stroke-width="3" stroke-linecap="round" stroke-linejoin="round"/></svg>
        <p class="sign__question">A Recognized Leader Amongst Other Experts?</p>
        <p class="sign__answer">I’m the 2018 duly elected President of the Empire Region Mental Health Guild Section on Courtroom Behavior, and a Board Member of the National Practitioners Council for Youth Welfare Protection.</p>
      </article>
      <article class="sign">
        <svg class="sign__tick" viewBox="0 0 28 28"><circle cx="14" cy="14" r="14" fill="#ec1f27"/><path d="M8 14.5l4 4 8-9" fill="none" stroke="#fff" stroke-width="3" stroke-linecap="round" stroke-linejoin="round"/></svg>
        <p class="sign__question">Positioned in Roles of Trust and Neutrality by Judges?</p>
        <p class="sign__answer">Yes, I work as an in-house Harbor County Domestic Tribunal mental-health expert in proceedings regarding competency, imminent risk, sentencing, custody, child maltreatment and TPR.</p>
      </article>
    </div>
  </section>

  <section class="panel panel--offer">
    <div class="hero" role="img" aria-label="Photo of a wood-panelled courtroom with brass scales of justice on the bench in the foreground"></div>
    <p class="hero__tagline">I recognize the importance of your work. You can trust my assistance.</p>
    <h2 class="cta__headline">BOOK A LUNCH<br>&amp; LEARN AT YOUR OFFICE</h2>
    <div class="cta__bar">
      <svg class="cta__shape" width="280" height="18" viewBox="0 0 280 18"><polygon points="0,0 280,0 268,18 0,18" fill="#ec1f27"/></svg>
      <span class="cta__contact cta__contact--web">
        <svg width="10" height="10" viewBox="0 0 10 10"><circle cx="5" cy="5" r="4.3" fill="none" stroke="#fff" stroke-width="1"/><ellipse cx="5" cy="5" rx="1.8" ry="4.3" fill="none" stroke="#fff" stroke-width="0.8"/><line x1="0.7" y1="5" x2="9.3" y2="5" stroke="#fff" stroke-width="0.8"/></svg>
        <span>Visit http://offer.benchwise-example.com</span>
      </span>
      <span class="cta__contact cta__contact--phone">
        <svg width="10" height="10" viewBox="0 0 10 10"><circle cx="5" cy="5" r="5" fill="#fff"/><path d="M3.2 2.6l1 1-0.6 0.8c0.4 0.9 1 1.5 1.9 1.9l0.8-0.6 1 1-0.7 0.9c-2 -0.3-3.9-2.2-4.2-4.2z" fill="#ec1f27"/></svg>
        <span>212-555-0147</span>
      </span>
    </div>
    <div class="specialties">
      <ul>
        <li>· CPS &amp; Matrimonial Issues</li>
        <li>· Competency</li>
        <li>· Juvenile Delinquency</li>
        <li>· Criminal Sentencing</li>
        <li>· Personal Injury and Civil Rights</li>
        <li>· Immigration</li>
      </ul>
      <ul>
        <li>· Fitness for Duty, SSD and Workers Comp</li>
        <li>· Sex-Offenders</li>
        <li>· IME and Neuropsychological Testing</li>
        <li>· Behind-The-Scenes Consulting on A Contingency Fee</li>
        <li>· Low-Price Initial Screening Evaluations</li>
        <li>· Therapy Services &amp; Programs for Litigants</li>
      </ul>
    </div>
    <p class="fine-print">Fenwick and Ostrander, LLC. 2018 New York Licensed Psychologist Lic. # 047213<br>New Jersey Licensed Psychologist Lic. # 72K400915300</p>
  </section>
</body>
</html>
```